looking for sleek business card to standout from the crowd!

We are a young biotechnology company looking to help you personalize your health through understanding your genetic make up. We need you help in making a clean but sleek business card design using our new logo. The goal? Any time we give our cards out, people say "nice card!" The feel we are going for is "modern-techy". We don't want to come across as an old, giant pharma company, but not trying to be a hipster either.

Target Market(s)

healthcare and biotechnology industry.

Industry/Entity Type

Biotechnology

Contact Information for Business Card

Info to include on the card will be NAME, TITLE, EMAIL, PHONE. The companies website (www.corvalinbio.com) should also be on the card some where. Would like the logo, when printed, to be raised.

Requirements
Must have
• The logo we have attached in the color it is in. Fonts for text should lean toward more professional/tech.
Nice to have
• Prefer white/light color background
Should not have
• cartoons, landscape backgrounds images.

```html
<!DOCTYPE html>
<html lang="en">
<head>
<meta charset="UTF-8">
<title>Corvalin Bio – Business Card</title>
<link rel="stylesheet" href="https://fonts.googleapis.com/css2?family=Federo&display=swap">
<style>
  :root {
    --brand-blue: #0a75bb;
    --brand-green: #8cc63f;
    --card-white: #ffffff;
    --ink: #2b2b2b;
    --ink-soft: #3a3a3a;
    --ink-muted: #6a6a6a;
  }
  html, body {
    margin: 0;
    padding: 0;
    width: 1200px;
    height: 686px;
    overflow: hidden;
    background: var(--card-white);
  }
  .card {
    position: relative;
    width: 1200px;
    height: 686px;
    background: var(--card-white);
    font-family: "Federo", sans-serif;
    color: var(--ink);
    overflow: hidden;
  }
  .card__shapes {
    position: absolute;
    inset: 0;
    width: 100%;
    height: 100%;
  }
  .card__person {
    position: absolute;
    top: 28px;
    right: 43px;
    text-align: right;
  }
  .card__name {
    margin: 0;
    font-size: 31px;
    font-weight: 400;
    line-height: 1.1;
    letter-spacing: 5px;
    color: var(--ink-soft);
  }
  .card__title {
    margin: 4px 0 0;
    font-size: 18px;
    font-weight: 400;
    letter-spacing: 3px;
    color: var(--ink-muted);
  }
  .brand {
    position: absolute;
    top: 222px;
    left: 0;
    width: 100%;
    text-align: center;
  }
  .brand__name {
    font-size: 80px;
    font-weight: 400;
    line-height: 1;
    letter-spacing: 2px;
    color: var(--brand-blue);
  }
  .card__website {
    position: absolute;
    top: 324px;
    left: 0;
    width: 100%;
    text-align: center;
    font-size: 38px;
    letter-spacing: 7px;
    color: #1f1f1f;
  }
  .contact {
    position: absolute;
    left: 377px;
    top: 418px;
    margin: 0;
    padding: 0;
    list-style: none;
  }
  .contact__item {
    display: flex;
    align-items: center;
    gap: 16px;
    height: 44px;
    margin-bottom: 10px;
    font-size: 31px;
    letter-spacing: 6px;
    color: #333;
  }
  .contact__icon {
    width: 42px;
    height: 42px;
    flex: none;
  }
</style>
</head>
<body>
<div class="card">
  <svg class="card__shapes" viewBox="0 0 1050 600" preserveAspectRatio="none" aria-hidden="true">
    <path d="M0,252 C90,132 200,50 322,0 L0,0 Z" fill="var(--brand-green)"/>
    <path d="M0,190 C100,95 205,35 342,0 L0,0 Z" fill="var(--brand-blue)"/>
    <path d="M1050,372 C960,480 855,555 735,600 L1050,600 Z" fill="var(--brand-green)"/>
    <path d="M1050,425 C975,505 880,565 785,600 L1050,600 Z" fill="var(--brand-blue)"/>
    <rect x="1.5" y="1.5" width="1047" height="597" fill="none" stroke="var(--brand-blue)" stroke-width="3"/>
  </svg>

  <div class="card__person">
    <h1 class="card__name">Meera Kadam</h1>
    <p class="card__title">Genetic Consultant</p>
  </div>

  <div class="brand">
    <span class="brand__name">CORVALIN</span>
  </div>

  <div class="card__website">www.corvalinbio.com</div>

  <ul class="contact">
    <li class="contact__item">
      <svg class="contact__icon" viewBox="0 0 42 42" aria-hidden="true">
        <circle cx="21" cy="21" r="18" fill="none" stroke="var(--brand-blue)" stroke-width="2"/>
        <path d="M15 12 l4 0 l1.5 5 l-2.5 2 q2 4 5 5.5 l2 -2.5 l5 1.5 l0 4 q-1 2 -4 2 q-8 -1 -12 -10 q-1 -4 1 -7.5 z" fill="var(--brand-blue)"/>
      </svg>
      <span>+91 98765 43210</span>
    </li>
    <li class="contact__item">
      <svg class="contact__icon" viewBox="0 0 42 42" aria-hidden="true">
        <rect x="4" y="10" width="34" height="24" fill="none" stroke="var(--brand-blue)" stroke-width="2"/>
        <path d="M4 10 L21 24 L38 10 M4 34 L16 20 M38 34 L26 20" fill="none" stroke="var(--brand-blue)" stroke-width="2"/>
      </svg>
      <span>hello@corvalinbio.com</span>
    </li>
  </ul>
</div>
</body>
</html>
```